Solvane Glow LED - E- Commerce site

We need a website designed for an LED Billboard company that sells:
1) LED Billboards (Sales & Rental)
2) LED Gas Station lights
3) Truss Systems (Sales & Rental)
4) Sound Systems (Sales & Rental)

Attached are websites that sell similar products as Solvane Glow LED. Target market is for business, property managers and event coordinators.
This site will need to be an e-commerce site where customers can purchase the product directly from the site. What I'm looking for is a design layout to start.

Conceptual Web Designs:
http://example-panelora.test/index.html
http://www.vormpix.com/
http://www.droneplayaudio.com/
http://www.quillmarkdisplay.com/

Attached is the logo of the company: Please note that the new spelling of the logo is "Solvane Glow LED" using domain " SolvaneGlowLED.com

Industry/Entity Type

Gas Station

Number of Pages Required

5+ page

Requirements
Must have
• 1) E-Commerce - Customers will need to be able to order product from the site.
• 2) Customers will also have the option to rent the product as well.
Nice to have
• I like the image of the attached website, that has a video clip loop
• http://www.quillmarkdisplay.com/

```html
<!DOCTYPE html>
<html lang="en">
<head>
<meta charset="utf-8">
<title>Solvane Glow LED</title>
<link rel="stylesheet" href="https://fonts.googleapis.com/css2?family=Audiowide&family=Lato:wght@400;700;900&display=swap">
<style>
:root{
  --ink:#1b1b1f;
  --nav:#141416;
  --red:#e0262d;
  --yellow:#e6b91e;
  --gold:#f5cf1c;
  --navy:#2a3188;
  --teal:#129fbf;
  --teal-dark:#0e87a4;
  --white:#ffffff;
  --grey:#555;
  --footer:#1c1c1e;
  --line:#e98b95;
}
*{box-sizing:border-box;margin:0;padding:0}
html,body{width:1200px;height:3125px;overflow:hidden}
body{font-family:"Lato",sans-serif;color:var(--ink);background:var(--white);position:relative}
.abs{position:absolute}

/* nav */
.topbar{left:0;top:0;width:1200px;height:60px;background:var(--nav)}
.brand-mini{left:80px;top:12px;display:flex;align-items:center;gap:6px;color:var(--gold);font-weight:900;font-size:13px}
.brand-mini i{width:22px;height:22px;border-radius:50%;border:3px solid var(--red);display:block}
.menu{left:245px;top:22px;display:flex;gap:28px;font-size:12px;color:var(--white);letter-spacing:.3px}
.menu .on{color:var(--red);position:relative}
.menu .on:after{content:"";position:absolute;left:2px;top:18px;width:36px;height:3px;background:linear-gradient(90deg,var(--red) 25%,var(--gold) 25% 50%,#3bb54a 50% 75%,#2f8fe0 75%)}
.search{left:828px;top:14px;width:192px;height:28px;background:#2c2c30;display:flex;align-items:center;justify-content:space-between;padding:0 10px;font-size:10px;color:#aaa}
.cart{left:1032px;top:8px;width:88px;height:44px;background:#232326;display:flex;align-items:center;justify-content:center;gap:8px;color:var(--white);font-size:13px}

/* hero */
.hero{left:0;top:60px;width:1200px;height:495px;background:linear-gradient(180deg,#120b22 0%,#2a1a4a 35%,#3a2a60 55%,#1c1430 72%,#0b0a14 100%)}
.hero-brand{left:85px;top:190px;display:flex;align-items:center;gap:18px;color:var(--gold);font-weight:900;font-size:44px;line-height:1.05}
.hero-brand i{width:70px;height:70px;border-radius:50%;border:8px solid var(--red);display:block;flex:none}
.lightup{left:492px;top:210px;font-family:"Audiowide",sans-serif;color:var(--white);font-size:30px}
.world{left:490px;top:250px;font-family:"Audiowide",sans-serif;color:var(--gold);font-size:72px;letter-spacing:2px}
.callnow{left:495px;top:376px;width:295px;height:76px;background:var(--red);display:flex;align-items:center;gap:14px;padding-left:18px;color:var(--white)}
.callnow .t{font-family:"Audiowide",sans-serif;font-size:20px;line-height:1}
.callnow .n{font-family:"Audiowide",sans-serif;font-size:28px;color:var(--gold);line-height:1.1}

/* sections */
.heading{left:0;width:1200px;text-align:center;font-family:"Audiowide",sans-serif;color:var(--navy);font-size:30px;letter-spacing:1px}
.rule{left:350px;width:500px;height:2px;background:var(--line)}
.whatwedo{left:0;top:555px;width:1200px;height:425px;background:var(--yellow)}
.copy{left:85px;top:685px;width:1030px;text-align:center;font-size:13px;line-height:23px;color:#2a2210}
.copy p+p{margin-top:23px}

.cards{left:80px;width:1040px;display:flex;justify-content:space-between}
.product{width:240px;height:295px;border:5px dotted var(--red);padding:8px;text-align:center;background:var(--white)}
.product:nth-child(2){border-color:#3bb54a}
.product:nth-child(3){border-color:#2f8fe0}
.product:nth-child(4){border-color:var(--gold)}
.product .ph{height:115px}
.product h3{font-size:15px;font-weight:700;margin:14px 0 6px;padding-bottom:6px;border-bottom:1px solid #ccc}
.product p{font-size:10.5px;line-height:15px;color:var(--grey);padding:0 6px}
.btn{display:inline-block;margin-top:12px;background:var(--red);color:var(--white);font-size:9px;font-weight:700;padding:5px 12px}

.specials{left:0;top:1460px;width:1200px;height:485px;background:var(--teal)}
.spec{width:240px;position:relative;text-align:center}
.spec .ring{width:134px;height:134px;margin:0 auto;border-radius:50%;border:3px solid #e9f6fa;padding:8px}
.spec .ring div{width:100%;height:100%;border-radius:50%;background:var(--teal-dark);display:flex;align-items:center;justify-content:center}
.spec .box{margin-top:10px;background:var(--white);height:170px;padding:28px 10px 0;position:relative}
.spec .box:before{content:"";position:absolute;left:108px;top:-12px;border:12px solid transparent;border-top:0;border-bottom-color:var(--white)}
.spec h3{font-size:16px;font-weight:700;letter-spacing:.5px}
.spec p{font-size:11px;line-height:21px;color:var(--grey);margin-top:6px}
.spec .more{font-size:9.5px;font-weight:900;margin-top:6px}

.tile{position:absolute}
.caption{left:16px;bottom:28px;width:250px;color:var(--gold);font-size:15px;line-height:23px;font-weight:700}

.newsletter{left:0;top:2816px;width:1200px;height:38px;background:var(--red)}
.nl-end{left:970px;top:2816px;width:230px;height:38px;background:var(--white);clip-path:polygon(30px 0,100% 0,100% 100%,0 100%)}
.nl{left:80px;top:2827px;display:flex;align-items:center;gap:12px;color:var(--white);font-size:13px}
.nl .f{width:215px;height:22px;background:var(--white);color:#aaa;font-size:9px;padding:5px 8px}
.nl .send{width:90px;height:22px;background:var(--gold);color:var(--ink);font-size:10px;font-weight:700;text-align:center;line-height:22px}
.social{left:1012px;top:2824px;display:flex;gap:7px}
.social i{display:block;width:24px;height:24px}

.footer{left:0;top:2854px;width:1200px;height:236px;background:var(--footer);color:#ddd}
.fcol{position:absolute;top:2885px;font-size:12px;line-height:23px}
.fcol h4{color:var(--gold);font-weight:400;font-size:13px;border-bottom:1px solid #555;margin-bottom:8px;padding-bottom:2px}
.fbrand{left:850px;top:2900px;display:flex;align-items:center;gap:14px;color:var(--gold);font-weight:900;font-size:30px;line-height:1.05}
.fbrand i{width:56px;height:56px;border-radius:50%;border:7px solid var(--red);display:block}
.bottom{left:0;top:3090px;width:1200px;height:35px;background:#111;color:#999;font-size:10px}
</style>
</head>
<body>

<header class="abs topbar"></header>
<div class="abs brand-mini"><i></i>Solvane Glow LED</div>
<nav class="abs menu"><span class="on">HOME</span><span>ABOUT US</span><span>LED DISPLAYS</span><span>SOLUTION</span><span>GALLERY</span><span>CONTACT US</span></nav>
<div class="abs search">Enter your Key words
<svg width="14" height="14" viewBox="0 0 14 14"><circle cx="6" cy="6" r="4.5" fill="none" stroke="#fff" stroke-width="2"/><path d="M9.5 9.5L13 13" stroke="#fff" stroke-width="2"/></svg></div>
<div class="abs cart"><svg width="22" height="18" viewBox="0 0 22 18"><path d="M1 2h4l3 10h10l2-7H7" fill="none" stroke="#fff" stroke-width="2"/><circle cx="9" cy="15.5" r="1.6" fill="#fff"/><circle cx="17" cy="15.5" r="1.6" fill="#fff"/></svg>(01)</div>

<section class="abs hero" role="img" aria-label="Night city skyline with lit towers reflected on the harbour"></section>
<div class="abs hero-brand"><i></i><span>Solvane Glow<br>LED</span></div>
<div class="abs lightup">LIGHT UP</div>
<div class="abs world">YOUR WORLD</div>
<div class="abs callnow">
  <svg width="36" height="36" viewBox="0 0 36 36"><circle cx="18" cy="18" r="16" fill="none" stroke="#fff" stroke-width="2"/><path d="M12 10l4 0 2 5-3 2c1 3 3 5 6 6l2-3 5 2v4c-9 1-17-7-16-16z" fill="#fff"/></svg>
  <div><div class="t">CALL NOW</div><div class="n">123 456 7890</div></div>
</div>

<section class="abs whatwedo"></section>
<h2 class="abs heading" style="top:595px">WHAT WE DO</h2>
<div class="abs rule" style="top:640px"></div>
<div class="abs copy">
<p>Lorem ipsum dolor sit amet, consectetur adipiscing elit. Donec facilisis est quis venenatis molestie. Maecenas nec nulla nibh. Nulla ut elementum metus. Proin imperdiet venenatis elit ac commodo. Cras eu nisi eu dolor aliquet vehicula vel at enim. Sed commodo euismod eros, eu fermentum purus bibendum sed. Integer ornare, turpis et vehicula elementum, augue lectus ornare tortor, nec accumsan nisl neque nec dui. Morbi volutpat, justo vitae ultricies pharetra, arcu tellus mollis lectus, nec tempor mi mauris sit amet augue. Morbi a neque lacus. Vestibulum metus lorem, tempor in pulvinar vel, dignissim eget nulla.Lorem ipsum dolor sit amet, consectetur adipiscing elit. Donec facilisis est quis venenatis molestie. Maecenas nec nulla nibh. Nulla ut elementum metus. Proin imperdiet venenatis elit ac commodo.</p>
<p>Cras eu nisi eu dolor aliquet vehicula vel at enim. Sed commodo euismod eros, eu fermentum purus bibendum sed. Integer ornare, turpis et vehicula elementum, augue lectus ornare tortor, nec accumsan nisl neque nec dui. Morbi volutpat, justo vitae ultricies pharetra, arcu tellus mollis lectus, nec tempor mi mauris sit amet augue. Morbi a neque lacus. Vestibulum metus lorem, tempor in pulvinar vel, dignissim eget nulla.<br>Pellentesque a felis eget dui vehicula euismod vel ac turpis. Quisque sed lacinia eros.</p>
</div>

<h2 class="abs heading" style="top:1022px">OUR PRODUCTS</h2>
<div class="abs rule" style="top:1068px"></div>
<div class="abs cards" style="top:1115px">
  <article class="product"><div class="ph" role="img" aria-label="LED billboard screens at night" style="background:linear-gradient(135deg,#1a1a2a,#6a4a5a,#20202e)"></div><h3>LED BILLBOARDS</h3><p>Lorem Ipsum is simply dummy text of the printing and typesetting industry. Lorem specimen book was popularised .</p><span class="btn">LEARN MORE</span></article>
  <article class="product"><div class="ph" role="img" aria-label="Lantern style light over green grass" style="background:linear-gradient(135deg,#4a6a2a,#7fa04a,#3a5a22)"></div><h3>LED GAS STATION LIGHTS</h3><p>Lorem Ipsum is simply dummy text of the printing and typesetting industry. Lorem specimen book was popularised .</p><span class="btn">LEARN MORE</span></article>
  <article class="product"><div class="ph" role="img" aria-label="Crew assembling a truss roof frame" style="background:linear-gradient(180deg,#8ab0d8,#b08060 60%,#6a5040)"></div><h3>TRUSS SYSTEMS</h3><p>Lorem Ipsum is simply dummy text of the printing and typesetting industry. Lorem specimen book was popularised .</p><span class="btn">LEARN MORE</span></article>
  <article class="product"><div class="ph" role="img" aria-label="Close-up of audio speaker equipment" style="background:linear-gradient(135deg,#222,#777,#2a2a2a)"></div><h3>SOUND SYSTEMS</h3><p>Lorem Ipsum is simply dummy text of the printing and typesetting industry. Lorem specimen book was popularised .</p><span class="btn">LEARN MORE</span></article>
</div>

<section class="abs specials"></section>
<h2 class="abs heading" style="top:1505px;color:var(--white)">OUR SPECIALITIES</h2>
<div class="abs rule" style="top:1550px;background:#0b6f88"></div>
<div class="abs cards" style="top:1582px">
  <div class="spec"><div class="ring"><div><svg width="60" height="60" viewBox="0 0 60 60" fill="none" stroke="#f5cf1c" stroke-width="4"><circle cx="24" cy="26" r="9"/><path d="M24 10v6M24 36v6M8 26h6M34 26h6M13 15l4 4M31 33l4 4M13 37l4-4M31 19l4-4"/><circle cx="44" cy="44" r="5"/></svg></div></div>
    <div class="box"><h3>TECHNOLOGY</h3><p>Lorem Ipsum is simply dummy text of the printing and typesetting the unknown printer took.</p><div class="more">READ MORE...</div></div></div>
  <div class="spec"><div class="ring"><div><svg width="56" height="60" viewBox="0 0 56 60"><path d="M28 4l22 8v16c0 14-10 24-22 28C16 52 6 42 6 28V12z" fill="#f5cf1c"/><path d="M28 10v40C19 46 12 38 12 28V16z" fill="#d9a90f"/></svg></div></div>
    <div class="box"><h3>WARRANTY</h3><p>Lorem Ipsum is simply dummy text of the printing and typesetting the unknown printer took.</p><div class="more">READ MORE...</div></div></div>
  <div class="spec"><div class="ring"><div><svg width="56" height="60" viewBox="0 0 56 60" fill="none" stroke="#f5cf1c" stroke-width="4"><path d="M20 40c0-6-8-10-8-18a16 16 0 0132 0c0 8-8 12-8 18z"/><path d="M21 46h14M23 52h10M28 0v4M6 8l3 3M50 8l-3 3"/></svg></div></div>
    <div class="box"><h3>SERVICE</h3><p>Lorem Ipsum is simply dummy text of the printing and typesetting the unknown printer took.</p><div class="more">READ MORE...</div></div></div>
  <div class="spec"><div class="ring"><div><svg width="60" height="60" viewBox="0 0 60 60"><path d="M30 4l6 5 8-1 2 8 7 4-3 7 3 7-7 4-2 8-8-1-6 5-6-5-8 1-2-8-7-4 3-7-3-7 7-4 2-8 8 1z" fill="#f5cf1c"/><circle cx="30" cy="30" r="13" fill="none" stroke="#0e87a4" stroke-width="3"/><path d="M23 30l5 5 9-10" fill="none" stroke="#0e87a4" stroke-width="4"/></svg></div></div>
    <div class="box"><h3>QUALITY</h3><p>Lorem Ipsum is simply dummy text of the printing and typesetting the unknown printer took.</p><div class="more">READ MORE...</div></div></div>
</div>

<h2 class="abs heading" style="top:1985px">FEATURED PRODUCTS</h2>
<div class="abs rule" style="top:2030px;background:linear-gradient(90deg,var(--line) 0 45%,var(--gold) 45% 60%,var(--line) 60%)"></div>
<div class="tile" role="img" aria-label="Cable bridge lit in purple at night over water" style="left:165px;top:2080px;width:580px;height:305px;background:linear-gradient(180deg,#1a1a4a 0%,#5a4a9a 55%,#6a3a7a 70%,#120f2a 100%)"></div>
<div class="tile" role="img" aria-label="Assorted LED bulbs with cooling chips" style="left:768px;top:2080px;width:280px;height:305px;background:linear-gradient(160deg,#7a7a70,#4a4a44 50%,#2e2e2a)"><div class="abs caption">VARIOUS LEDS BULB GU10 AND E27 WITH DIFFERENT COOLING SMD CHIPS</div></div>
<div class="tile" role="img" aria-label="Glowing LED bulb held close up" style="left:165px;top:2410px;width:275px;height:305px;background:radial-gradient(circle at 60% 55%,#ffe3b0,#e0703a 35%,#6a1a2a 75%,#2a0a1a)"></div>
<div class="tile" role="img" aria-label="White interior with pendant lamps and wooden floor" style="left:463px;top:2410px;width:280px;height:305px;background:linear-gradient(180deg,#f2f0ec 0%,#e4e2de 60%,#8a5a3a 72%,#5a3a22 100%)"></div>
<div class="tile" role="img" aria-label="Stadium floodlights over a football pitch" style="left:768px;top:2410px;width:280px;height:305px;background:linear-gradient(180deg,#0c1a3a 0%,#3a6aa0 40%,#d8e6f0 52%,#2a7a3a 70%,#145a22 100%)"></div>

<div class="abs newsletter"></div>
<div class="abs nl-end"></div>
<div class="abs nl"><span>NEWSLETTER</span><span class="f">Name</span><span class="f">Email ID</span><span class="send">SEND</span></div>
<div class="abs social"><i style="background:#3b5a9a"></i><i style="background:#c8232c"></i><i style="background:#333"></i></div>

<footer class="abs footer"></footer>
<div class="fcol" style="left:80px;width:140px"><h4>QUICK LINKS</h4>Home<br>About Us<br>LED Displays<br>Solution<br>Gallery<br>Contact us</div>
<div class="fcol" style="left:292px;width:225px"><h4>SHOWROOM</h4>gddgdgshg bdddhd<br>Lindqvist gate 18<br>0418 Varnholm
  <h4 style="margin-top:8px">OPENING HOURS</h4>Monday to Friday: 10:00 to 18:00<br>Saturday: 11:00 to 16:00<br><span style="color:var(--red)">Sunday closed</span></div>
<div class="fcol" style="left:570px;width:220px"><h4>ADDRESS</h4>svfsfsf vdsgbshgsd ndhndjndf<br>Tel.: +123 456 7890<br>Email: post@solvaneglowled.com</div>
<div class="abs fbrand"><i></i><span>Solvane Glow<br>LED</span></div>
<div class="abs bottom"><span class="abs" style="left:80px;top:12px">Copyright solvaneglowled.com. All rights reserved.</span><span class="abs" style="left:900px;top:12px">Terms &amp; Conditions &nbsp;&nbsp;|&nbsp;&nbsp; Delivery conditions</span></div>

</body>
</html>
```